Letterhead & Business Card Design Project

Use existing logo to create a new letterhead and business card design. Looking for something clean modern using color options of black, white and gray. The green from the logo may be used lightly as an accent color.

Target Market(s)

Professional business people

Industry/Entity Type

Business

Requirements
Must have
• Business card with front and back design using existing logo.
Nice to have
• Professional presentation
Clean look
Should not have
• No oil rigs, pumpjacks or clip art.

```html
<!DOCTYPE html>
<html lang="en">
<head>
<meta charset="utf-8">
<title>Halden Resources – Stationery</title>
<link rel="stylesheet" href="https://fonts.googleapis.com/css2?family=Questrial&display=swap">
<style>
  :root {
    --backdrop: #737478;
    --backdrop-edge: #5d5e61;
    --paper: #ffffff;
    --card-light: #e6e6e6;
    --card-light-edge: #9a9a9a;
    --card-dark: #353435;
    --accent: #0cbf0c;
    --ink: #111111;
    --ink-light: #ffffff;
  }
  * { box-sizing: border-box; margin: 0; padding: 0; }
  html, body { width: 1200px; height: 1029px; overflow: hidden; }
  body {
    position: relative;
    background: var(--backdrop);
    border: 1px solid var(--backdrop-edge);
    font-family: "Questrial", "Century Gothic", sans-serif;
    color: var(--ink);
  }

  /* Letterhead */
  .letterhead {
    position: absolute; left: 438px; top: 72px;
    width: 728px; height: 941px;
    background: var(--paper);
  }
  .accent-bar {
    position: absolute; top: 25px; width: 24px; height: 891px;
    background: var(--accent);
  }
  .accent-bar.left { left: 0; }
  .accent-bar.right { right: 0; }

  .wordmark { text-align: center; font-weight: 400; }
  .wordmark .name-main { display: block; line-height: 1; }
  .wordmark .name-sub { display: block; line-height: 1; }

  .letterhead .wordmark { position: absolute; left: 0; right: 0; top: 36px; }
  .letterhead .name-main { font-size: 62px; letter-spacing: 8px; }
  .letterhead .name-sub { font-size: 28px; letter-spacing: 13px; margin-top: 24px; }

  .contact-block {
    position: absolute; right: 41px; bottom: 8px;
    font-size: 13px; line-height: 17px; text-align: right;
  }
  .address-line {
    position: absolute; left: 75px; bottom: 8px;
    font-size: 13px; line-height: 17px;
  }
  .icon { display: inline-block; vertical-align: -2px; margin-right: 3px; fill: var(--ink); }

  /* Business cards */
  .card {
    position: absolute; left: 60px; width: 300px; height: 192px;
    border-radius: 20px; overflow: hidden;
  }
  .card.front { top: 255px; background: var(--card-light); border: 1px solid var(--card-light-edge); }
  .card.back { top: 486px; background: var(--card-dark); color: var(--ink-light); }
  .card .accent-bar { top: 32px; width: 5px; height: 126px; }
  .card .wordmark { position: absolute; left: 0; right: 0; }
  .card.front .wordmark { top: 26px; }
  .card.back .wordmark { top: 56px; }
  .card .name-main { font-size: 40px; letter-spacing: 5px; }
  .card .name-sub { font-size: 17px; letter-spacing: 7px; margin-top: 10px; }

  .card-contact {
    position: absolute; left: 0; right: 0; top: 134px;
    text-align: center; font-size: 7.5px; line-height: 13px;
  }
  .card-contact .icon { vertical-align: -1px; margin-right: 2px; }
</style>
</head>
<body>

  <section class="card front" aria-label="Business card front">
    <div class="accent-bar left"></div>
    <div class="accent-bar right"></div>
    <div class="wordmark">
      <span class="name-main">HALDEN</span>
      <span class="name-sub">resources</span>
    </div>
    <div class="card-contact">
      <div><svg class="icon" width="9" height="8" viewBox="0 0 16 14"><path d="M8 0 0 7h2v7h4V9h4v5h4V7h2z"/></svg></div>
      <div>4420 North Ridge Ave Suite 310 Tulsa, Oklahoma 74105</div>
      <div>
        <svg class="icon" width="7" height="8" viewBox="0 0 12 14"><path d="M3 0 0 2c0 6 4 11 9 12l3-3-3-3-2 1C5 8 4 6 4 5l2-1z"/></svg>918.555.0142
        &nbsp;<svg class="icon" width="8" height="8" viewBox="0 0 14 14"><path d="M3 0h7v4H3zM0 5h14v9H0zm3 3v2h8V8z"/></svg>Fax 918.555.0143
      </div>
      <div><svg class="icon" width="8" height="8" viewBox="0 0 14 14"><path d="M7 0a7 7 0 1 0 4 12.7l-1-1.4A5.3 5.3 0 1 1 12.3 7v1a1.3 1.3 0 0 1-2.6 0V4H8.3v.5A3.2 3.2 0 1 0 9 9.4 2.9 2.9 0 0 0 14 8V7a7 7 0 0 0-7-7zm0 8.8A1.8 1.8 0 1 1 7 5.2a1.8 1.8 0 0 1 0 3.6z"/></svg>www.haldenresources.com</div>
    </div>
  </section>

  <section class="card back" aria-label="Business card back">
    <div class="accent-bar left"></div>
    <div class="accent-bar right"></div>
    <div class="wordmark">
      <span class="name-main">HALDEN</span>
      <span class="name-sub">resources</span>
    </div>
  </section>

  <section class="letterhead" aria-label="Letterhead">
    <div class="accent-bar left"></div>
    <div class="accent-bar right"></div>
    <div class="wordmark">
      <span class="name-main">HALDEN</span>
      <span class="name-sub">resources</span>
    </div>
    <div class="address-line">
      <svg class="icon" width="14" height="12" viewBox="0 0 16 14"><path d="M8 0 0 7h2v7h4V9h4v5h4V7h2z"/></svg>4420 North Ridge Ave Suite 310 Tulsa, Oklahoma 74105
    </div>
    <div class="contact-block">
      <div><svg class="icon" width="11" height="13" viewBox="0 0 12 14"><path d="M3 0 0 2c0 6 4 11 9 12l3-3-3-3-2 1C5 8 4 6 4 5l2-1z"/></svg>Phone 918.555.0142</div>
      <div><svg class="icon" width="12" height="12" viewBox="0 0 14 14"><path d="M3 0h7v4H3zM0 5h14v9H0zm3 3v2h8V8z"/></svg>Fax 918.555.0143</div>
      <div><svg class="icon" width="13" height="13" viewBox="0 0 14 14"><path d="M7 0a7 7 0 1 0 4 12.7l-1-1.4A5.3 5.3 0 1 1 12.3 7v1a1.3 1.3 0 0 1-2.6 0V4H8.3v.5A3.2 3.2 0 1 0 9 9.4 2.9 2.9 0 0 0 14 8V7a7 7 0 0 0-7-7zm0 8.8A1.8 1.8 0 1 1 7 5.2a1.8 1.8 0 0 1 0 3.6z"/></svg>www.haldenresources.com</div>
    </div>
  </section>

</body>
</html>
```